New Letterhead request for our Law Firm!

We are a small Estate Planning Firm who just got out logo redesigned. It's attached. We need some letterhead for our client welcome letters and so forth. Clean, bright, and approachable is our style. If you need the specifications for our color scheme or other versions of the logo file, we have those too. Visit our website to get an idea about our services/aesthetics:https://willowmere.law/

Target Market(s)

Adults 30-80

Colors

Designer to choose colors to be used in the design.

Requirements
Must have
• Logo with color. Contact information

```html
<!DOCTYPE html>
<html lang="en">
<head>
<meta charset="utf-8">
<title>Willowmere Law Firm Letterhead</title>
<link href="https://fonts.googleapis.com/css2?family=Crimson+Text:wght@400;700&family=Roboto:ital,wght@0,400;1,300&display=swap" rel="stylesheet">
<style>
  :root {
    --backdrop: #6fa3a3;
    --paper: #ffffff;
    --brand-green: #5a9a78;
    --leaf-green: #7fae8e;
    --leaf-deep: #5f8a70;
    --ink: #3a3a3a;
    --ink-soft: #6a6a6a;
    --band: #444444;
  }
  * { box-sizing: border-box; margin: 0; padding: 0; }
  html, body { width: 1200px; height: 1138px; overflow: hidden; }
  body { background: var(--backdrop); position: relative; }
  .letter {
    position: absolute; left: 190px; top: 39px; width: 820px; height: 1060px;
    background: var(--paper); box-shadow: 0 10px 30px rgba(0,0,0,.18);
  }
  .brand { position: absolute; left: 70px; top: 62px; display: flex; align-items: center; gap: 16px; }
  .brand-mark { width: 64px; height: 64px; border: 3px solid var(--brand-green); border-radius: 50%; }
  .brand-name {
    font-family: "Crimson Text", serif; font-weight: 700; color: var(--brand-green);
    font-size: 34px; line-height: 1; letter-spacing: 1px;
  }
  .brand-name small { display: block; font-size: 16px; letter-spacing: 3px; margin-top: 2px; }
  .contact {
    position: absolute; left: 70px; top: 150px;
    font-family: "Roboto", sans-serif; font-style: italic; font-weight: 300;
    font-size: 13px; line-height: 20px; color: var(--ink-soft);
  }
  .salutation {
    position: absolute; left: 310px; top: 300px;
    font-family: "Crimson Text", serif; font-size: 20px; color: var(--brand-green);
  }
  .body-copy {
    position: absolute; left: 310px; top: 345px; width: 430px;
    font-family: "Roboto", sans-serif; font-size: 11px; line-height: 16px; color: var(--ink);
  }
  .body-copy p { margin-bottom: 12px; text-align: justify; }
  .signature {
    position: absolute; left: 310px; top: 672px; width: 220px; height: 50px;
    background: linear-gradient(90deg, #e4e4e4, #f2f2f2); border-radius: 4px;
  }
  .signatory { position: absolute; left: 310px; top: 732px; font-family: "Crimson Text", serif; }
  .signatory .name { font-size: 19px; color: var(--brand-green); }
  .signatory .title { font-family: "Roboto", sans-serif; font-style: italic; font-weight: 300; font-size: 13px; color: var(--ink-soft); margin-top: 2px; }
  .tree-art {
    position: absolute; left: 45px; top: 878px; width: 110px; height: 92px;
    border-radius: 50% 50% 45% 45%;
    background: radial-gradient(ellipse at 50% 40%, var(--leaf-green) 0%, var(--leaf-deep) 100%);
  }
  .footer-band { position: absolute; left: 40px; right: 0; top: 975px; height: 14px; background: var(--band); }
</style>
</head>
<body>
  <main class="letter">
    <header class="brand">
      <div class="brand-mark"></div>
      <div class="brand-name">WILLOWMERE<small>LAW FIRM</small></div>
    </header>
    <address class="contact">
      2480 Lakeview Parkway,<br>
      Suite 310, Brookdale, MN 55420<br>
      T: 612 555 0148<br>
      E: info@willowmere.law<br>
      www.willowmere.law
    </address>
    <p class="salutation">Dear Mr. Thomas Reed</p>
    <section class="body-copy">
      <p>Lorem ipsum dolor sit amet, consectetur adipiscing elit. Quisque sagittis, sapien id placerat cursus, purus turpis ultrices lectus, a dictum tellus magna eget nulla. Nulla at tortor quis diam maximus tempus. Ut at dui eget lorem molestie elementum. Phasellus egestas metus a magna imperdiet, a vehicula sapien commodo. In tellus nisi, dapibus venenatis finibus nec, lobortis eu nisl. Curabitur pellentesque sapien sed erat ullamcorper aliquam. Morbi sed placerat nisi, ut elementum tellus.</p>
      <p>Proin laoreet dui vel congue cursus. Duis ultricies neque quis sapien rutrum, id euismod nunc hendrerit. Nulla euismod quam nibh, ut elementum tortor finibus eget. Nunc tempor libero placerat mauris aliquet euismod. Integer in mauris nec neque elementum iaculis.</p>
      <p>Donec suscipit nunc in nisi imperdiet, vitae egestas justo tempus. Vivamus pretium congue gravida. Curabitur ornare est ac tellus malesuada dictum. Quisque eget enim hendrerit, porttitor urna vitae, varius enim. In tempus sit amet arcu eget auctor. Maecenas posuere pharetra massa id malesuada.</p>
      <p>Duis ultricies neque quis sapien rutrum, id euismod nunc hendrerit. Nulla euismod quam nibh, ut elementum tortor finibus eget. Nunc tempor libero placerat mauris aliquet euismod. Integer in mauris nec neque elementum iaculis.</p>
    </section>
    <div class="signature" role="img" aria-label="Handwritten signature of Helena Marsh"></div>
    <div class="signatory">
      <div class="name">Helena Marsh</div>
      <div class="title">Attorney/Lawyer</div>
    </div>
    <div class="tree-art" role="img" aria-label="Illustration of a small leafy tree"></div>
    <div class="footer-band"></div>
  </main>
</body>
</html>
```